Layout für Longboardshop
Zielgruppe
Online Shop für Longboards, basierend auf Ladenwerk 4.1.2
Zielgruppe: Sportliche Menschen mit Hang zum Wellenreiten, Surfen,Kiten, Snowboarden oder Skateboarden.
Aufgabenstellung
Erstellung des Grunddesigns (Header, Footer, Menü, Detailansicht, Buttons) als PSD. Die Umsetzung in ein Template erledigen wir alleine.
Neugründung: Es existieren noch keine Logos oder Farbvorgaben.
We have no site, it is a completly new project. There are no limits concerning colors, fonts etc.
Competitors:
http://www.brettfahrer-welt.de
http://wilhelmine-bretter.de/
http://www.rollbrettladen.de/
http://www.kavero.de/de_DE/Skateboard/Longboards.html?sid=1
http://www.pirumo-bretter.de/
I think, big pictures transporting the surfstyle attitude of this sport works good.
Der Grundaufbau sollte sich an http://www.ladenwerkdemo.de/ anlehnen, um den Anpassungsaufwand mgl. überschaubar zu halten.

```html
<!DOCTYPE html>
<html lang="de">
<head>
<meta charset="utf-8">
<title>Wellenbrett – Longboard Shop</title>
<link href="https://fonts.googleapis.com/css2?family=Source+Sans+3:wght@400;600;700;900&display=swap" rel="stylesheet">
<style>
:root{
  --blue:#1a86aa;
  --blue-dark:#116a8c;
  --topbar:#1f6a9c;
  --topbar-edge:#14507a;
  --grey-btn:#555;
  --panel:#fff;
  --text:#1c1c1c;
  --footer:#242424;
  --arrow-grey:#a9a9a9;
  --link:#1fa0c8;
}
*{margin:0;padding:0;box-sizing:border-box}
html,body{width:1200px;height:1140px;overflow:hidden}
body{position:relative;font-family:"Source Sans 3",Arial,sans-serif;font-weight:400;color:var(--text);
  background:radial-gradient(ellipse at 50% 30%,#ececec 0%,#dedede 70%,#d6d6d6 100%)}
.abs{position:absolute}

/* top bar */
.topbar{left:0;top:0;width:1200px;height:25px;background:var(--topbar);border-top:3px solid var(--topbar-edge)}
.topnav{position:absolute;right:241px;top:0;height:22px;display:flex}
.topnav a{display:flex;align-items:center;gap:6px;padding:0 10px;color:#fff;font-size:8.5px;text-decoration:none;border-left:1px solid rgba(255,255,255,.18)}
.topnav a:last-child{border-right:1px solid rgba(255,255,255,.18)}
.topnav svg{width:10px;height:10px;fill:#fff}
.flag{width:13px;height:8px;display:flex;flex-direction:column}
.flag i{flex:1}

/* header */
.brand{left:262px;top:22px;display:flex;align-items:center;gap:8px;color:var(--blue);font-weight:900;font-size:26px;letter-spacing:.5px}
.brand .mark{width:16px;height:16px;background:var(--blue)}
.search{left:514px;top:59px;width:120px;height:15px;background:#fff;border-radius:8px;box-shadow:inset 0 1px 2px rgba(0,0,0,.25);font-size:7px;font-style:italic;color:#777;padding:3px 0 0 13px}
.search svg{position:absolute;right:6px;top:4px;width:7px;height:7px}
.seal{left:668px;top:55px;width:23px;height:23px;border-radius:50%;background:#5a5a5a;border:2px solid #999}
.seal-text{left:695px;top:57px;font-size:6.5px;line-height:9.5px;color:#888}
.seal-text b{color:#777}
.cart{left:790px;top:41px;width:170px;height:38px;background:var(--blue);display:flex;align-items:center;color:#fff}
.cart svg{margin-left:34px;width:20px;height:26px}
.cart .label{margin-left:14px;font-size:8.5px;font-weight:700}
.cart .count{margin-left:14px;width:16px;height:16px;border-radius:50%;background:#fff;color:var(--text);font-size:7px;display:flex;align-items:center;justify-content:center}
.cart-info{left:790px;top:80px;width:170px;height:15px;background:var(--blue);color:#fff;font-size:7.8px;text-align:center;line-height:15px}

/* main nav */
.mainnav{top:114px;height:23px;background:linear-gradient(#1f95ba,#137a9d)}
.mainnav a{position:absolute;top:0;height:23px;line-height:23px;color:#fff;font-size:8.5px;font-weight:700;text-decoration:none;transform:translateX(-50%)}
.mainnav .sep{position:absolute;top:0;width:1px;height:23px;background:rgba(0,0,0,.18)}
.tab{background:var(--panel)}
.outline-btn{border:1px solid var(--blue);color:var(--blue-dark);font-size:8.5px;font-weight:600;text-align:center;background:#fff}

/* hero panel */
.hero-panel{left:240px;top:137px;width:720px;height:240px;background:var(--panel)}
.panel-shadow{left:250px;top:376px;width:700px;height:6px;background:radial-gradient(ellipse at 50% 0,rgba(0,0,0,.35),rgba(0,0,0,0) 70%)}
.hero{left:258px;top:156px;width:473px;height:199px;background:linear-gradient(135deg,#6fc0e6 0%,#1e78b4 45%,#0d4f86 70%,#4aa6d8 100%)}
.hero-copy{position:absolute;right:21px;top:84px;text-align:right;color:#fff;font-weight:900;letter-spacing:-1.5px;line-height:31px;font-size:37px}
.teaser-a{left:739px;top:156px;width:200px;height:95px;background:linear-gradient(180deg,#2b6a86 0%,#6aa9b8 45%,#f2e6a8 70%,#1a1f24 100%)}
.teaser-b{left:739px;top:259px;width:200px;height:96px;background:linear-gradient(160deg,#b49bb8 0%,#f3c6a5 45%,#fbe3b0 60%,#f0904a 100%)}

/* product rows */
.row-panel{background:var(--panel)}
.ribbon{left:240px;top:399px;width:36px;height:252px}
.ribbon-text{position:absolute;left:8px;top:70px;width:12px;color:#fff;font-weight:700;font-size:10px;line-height:11.6px;text-align:center}
.arrow-col{width:24px}
.arrow-col.up{background:var(--arrow-grey)}
.arrow-col.down{background:linear-gradient(#1888ad,#106f93)}
.arrow-col svg{position:absolute;left:8px;width:8px;height:10px}

.card{position:absolute;width:170px;text-align:center}
.photo{height:150px;display:flex;justify-content:center;align-items:center;gap:6px}
.card h3{font-size:11.5px;font-weight:600;margin-top:14px;letter-spacing:-.2px;line-height:14px}
.card p{font-size:7.6px;line-height:10.5px;font-weight:400}
.card p b{font-weight:700}
.buttons{display:flex;justify-content:center;gap:3px;margin-top:6px}
.btn{height:21px;line-height:21px;color:#fff;font-size:7.6px;font-weight:600}
.btn.details{width:40px;background:var(--grey-btn)}
.btn.add{width:85px;background:linear-gradient(#1d93b8,#14789b)}

.deck{width:38px;height:146px;border-radius:19px / 36px;background:var(--c)}
.truck{width:124px;height:42px;border-radius:8px;background:linear-gradient(#eee,#9a9a9a)}
.wheel{width:100px;height:100px;border-radius:50%;background:radial-gradient(circle,#555 0 20%,#f4f4f4 22% 100%);box-shadow:0 0 0 1px #ddd}

/* footer */
.footer-band{left:0;top:996px;width:1200px;height:7px;background:var(--blue)}
.footer{left:0;top:1003px;width:1200px;height:122px;background:var(--footer);color:#fff}
.footer h4{position:absolute;top:24px;font-size:8.5px;font-weight:400}
.footer h4 span{color:var(--link)}
.flist{position:absolute;top:49px;font-size:8.3px;line-height:15.6px;list-style:none;font-weight:400}
.flist a{color:var(--link);text-decoration:none}
.ftext{position:absolute;left:751px;top:49px;width:212px;font-size:8.3px;line-height:15.6px;font-weight:400}
.copyright{left:0;top:1125px;width:1200px;height:15px;background:var(--topbar);color:#fff;font-size:7.5px;text-align:center;line-height:15px}
</style>
</head>
<body>

<div class="abs topbar">
  <nav class="topnav">
    <a href="#"><svg viewBox="0 0 10 10"><circle cx="5" cy="3" r="2.5"/><path d="M0 10c0-3 2-4.5 5-4.5s5 1.5 5 4.5z"/></svg>Mein Konto</a>
    <a href="#"><svg viewBox="0 0 10 10"><path d="M2 1h6v9H2z" fill="none" stroke="#fff"/><path d="M3.5 5l1.2 1.2L7 4" fill="none" stroke="#fff"/></svg>Merkzettel</a>
    <a href="#"><svg viewBox="0 0 10 10"><path d="M1 9l5-5M4 9L9 4M2 1l7 7" stroke="#fff" stroke-width="1.4"/></svg>Service/Hilfe</a>
    <a href="#"><svg viewBox="0 0 10 10"><path d="M1 3l4 4 4-4" fill="none" stroke="#fff" stroke-width="1.6"/></svg>EUR</a>
    <a href="#"><svg viewBox="0 0 10 10"><path d="M1 3l4 4 4-4" fill="none" stroke="#fff" stroke-width="1.6"/></svg><span class="flag"><i style="background:#000"></i><i style="background:#d00"></i><i style="background:#fc0"></i></span></a>
  </nav>
</div>

<div class="abs brand"><span class="mark"></span>WELLENBRETT</div>

<div class="abs search">Suchbegriff<svg viewBox="0 0 8 8"><circle cx="3.2" cy="3.2" r="2.4" fill="none" stroke="#999"/><path d="M5 5l2.5 2.5" stroke="#999"/></svg></div>
<div class="abs seal"></div>
<div class="abs seal-text"><b>Sicher</b> einkaufen<br>Kaufsiegel zertifiziert</div>

<div class="abs cart">
  <svg viewBox="0 0 20 26"><path d="M2 8h16l-1 17H3z" fill="#d8d8d8"/><path d="M6 9V5a4 4 0 0 1 8 0v4" fill="none" stroke="#d8d8d8" stroke-width="1.4"/></svg>
  <span class="label">WARENKORB</span><span class="count">2</span>
</div>
<div class="abs cart-info">Es befinden sich <b>2 Artikel</b> im Warenkorb.</div>

<div class="abs tab" style="left:240px;top:108px;width:68px;height:30px"></div>
<nav class="abs mainnav" style="left:308px;width:652px">
  <a href="#" style="left:55px">DECKS</a>
  <span class="sep" style="left:107px"></span>
  <a href="#" style="left:162px">ZUBEHÖR</a>
  <span class="sep" style="left:219px"></span>
  <a href="#" style="left:271px">% SALE</a>
  <span class="sep" style="left:324px"></span>
  <a href="#" style="left:367px">TEAM</a>
  <span class="sep" style="left:414px"></span>
  <a href="#" style="left:468px">BILDER</a>
  <span class="sep" style="left:523px"></span>
  <a href="#" style="left:586px">KONTAKT</a>
</nav>
<div class="abs outline-btn" style="left:248px;top:115px;width:51px;height:20px;line-height:18px">HOME</div>

<section class="abs hero-panel"></section>
<div class="abs hero" role="img" aria-label="Foto: Surfbrett von unten in schäumender blauer Welle">
  <div class="hero-copy">-10%<br>AUF ALLE<br>BOARDS</div>
</div>
<div class="abs teaser-a" role="img" aria-label="Foto: Skater als Silhouette im Gegenlicht auf einem Geländer"></div>
<div class="abs teaser-b" role="img" aria-label="Foto: Skater springt vor orangem Abendhimmel"></div>
<div class="abs panel-shadow"></div>

<!-- topseller -->
<section class="abs row-panel" style="left:240px;top:399px;width:696px;height:252px"></section>
<div class="abs ribbon">
  <svg width="36" height="252" viewBox="0 0 36 252" style="position:absolute;left:0;top:0"><defs><linearGradient id="rib" x1="0" y1="0" x2="0" y2="1"><stop offset="0" stop-color="#1b8fb5"/><stop offset="1" stop-color="#0f6e92"/></linearGradient></defs><path d="M0 0h24l12 126-12 126H0z" fill="url(#rib)"/></svg>
  <div class="ribbon-text">T O P S E L L E R</div>
</div>
<div class="abs arrow-col up" style="left:936px;top:399px;height:124px"><svg viewBox="0 0 8 10" style="top:57px"><path d="M6 1L2 5l4 4" fill="none" stroke="#fff" stroke-width="2"/></svg></div>
<div class="abs arrow-col down" style="left:936px;top:523px;height:128px"><svg viewBox="0 0 8 10" style="top:59px"><path d="M2 1l4 4-4 4" fill="none" stroke="#fff" stroke-width="2"/></svg></div>

<div class="card" style="left:272px;top:412px"><div class="photo" role="img" aria-label="Produktfoto: Longboard Deck, Ober- und Unterseite"><span class="deck" style="--c:#41454b"></span><span class="deck" style="--c:linear-gradient(160deg,#2b8c9e,#d94b6e)"></span></div><h3>ARTIKELBEZEICHNUNG</h3><p>Lorem Ipsum. Proin gravidanv.<br>Preis: <b>123,00€</b> inkl. MwSt.</p><div class="buttons"><span class="btn details">DETAILS</span><span class="btn add">IN DEN WARENKORB</span></div></div>
<div class="card" style="left:433px;top:412px"><div class="photo" role="img" aria-label="Produktfoto: Longboard aus Holz"><span class="deck" style="--c:#c49a6c"></span><span class="deck" style="--c:linear-gradient(160deg,#b59a7a,#6f6a5a)"></span></div><h3>ARTIKELBEZEICHNUNG</h3><p>Lorem Ipsum. Proin gravidanv.<br>Preis: <b>123,00€</b> inkl. MwSt.</p><div class="buttons"><span class="btn details">DETAILS</span><span class="btn add">IN DEN WARENKORB</span></div></div>
<div class="card" style="left:599px;top:412px"><div class="photo" role="img" aria-label="Produktfoto: schwarzes Longboard mit gelben Achsen"><span class="deck" style="--c:#3a3a3a"></span><span class="deck" style="--c:linear-gradient(160deg,#caa050,#3a3530)"></span></div><h3>ARTIKELBEZEICHNUNG</h3><p>Lorem Ipsum. Proin gravidanv.<br>Preis: <b>123,00€</b> inkl. MwSt.</p><div class="buttons"><span class="btn details">DETAILS</span><span class="btn add">IN DEN WARENKORB</span></div></div>
<div class="card" style="left:764px;top:412px"><div class="photo" role="img" aria-label="Produktfoto: Longboard in Grün, Gelb und Rot"><span class="deck" style="--c:linear-gradient(#2f9a55,#e3c93b 50%,#d8453a 85%,#444)"></span><span class="deck" style="--c:linear-gradient(#2f9a55,#e3c93b 50%,#d8453a 85%)"></span></div><h3>ARTIKELBEZEICHNUNG</h3><p>Lorem Ipsum. Proin gravidanv.<br>Preis: <b>123,00€</b> inkl. MwSt.</p><div class="buttons"><span class="btn details">DETAILS</span><span class="btn add">IN DEN WARENKORB</span></div></div>

<!-- alle artikel -->
<div class="abs tab" style="left:240px;top:660px;width:101px;height:26px"></div>
<div class="abs outline-btn" style="left:250px;top:665px;width:81px;height:19px;line-height:17px">ALLE ARTIKEL</div>
<section class="abs row-panel" style="left:240px;top:685px;width:696px;height:252px"></section>
<div class="abs arrow-col up" style="left:936px;top:685px;height:124px"><svg viewBox="0 0 8 10" style="top:57px"><path d="M6 1L2 5l4 4" fill="none" stroke="#fff" stroke-width="2"/></svg></div>
<div class="abs arrow-col down" style="left:936px;top:809px;height:128px"><svg viewBox="0 0 8 10" style="top:59px"><path d="M2 1l4 4-4 4" fill="none" stroke="#fff" stroke-width="2"/></svg></div>

<div class="card" style="left:256px;top:698px"><div class="photo" role="img" aria-label="Produktfoto: silberne Longboard-Achse"><span class="truck"></span></div><h3>ARTIKELBEZEICHNUNG</h3><p>Lorem Ipsum. Proin gravidanv.<br>Preis: <b>123,00€</b> inkl. MwSt.</p><div class="buttons"><span class="btn details">DETAILS</span><span class="btn add">IN DEN WARENKORB</span></div></div>
<div class="card" style="left:421px;top:698px"><div class="photo" role="img" aria-label="Produktfoto: Longboard aus Holz"><span class="deck" style="--c:#c49a6c"></span><span class="deck" style="--c:linear-gradient(160deg,#b59a7a,#6f6a5a)"></span></div><h3>ARTIKELBEZEICHNUNG</h3><p>Lorem Ipsum. Proin gravidanv.<br>Preis: <b>123,00€</b> inkl. MwSt.</p><div class="buttons"><span class="btn details">DETAILS</span><span class="btn add">IN DEN WARENKORB</span></div></div>
<div class="card" style="left:587px;top:698px"><div class="photo" role="img" aria-label="Produktfoto: schwarzes Longboard mit gelben Achsen"><span class="deck" style="--c:#3a3a3a"></span><span class="deck" style="--c:linear-gradient(160deg,#caa050,#3a3530)"></span></div><h3>ARTIKELBEZEICHNUNG</h3><p>Lorem Ipsum. Proin gravidanv.<br>Preis: <b>123,00€</b> inkl. MwSt.</p><div class="buttons"><span class="btn details">DETAILS</span><span class="btn add">IN DEN WARENKORB</span></div></div>
<div class="card" style="left:750px;top:698px"><div class="photo" role="img" aria-label="Produktfoto: weiße Skateboard-Rolle"><span class="wheel"></span></div><h3>ARTIKELBEZEICHNUNG</h3><p>Lorem Ipsum. Proin gravidanv.<br>Preis: <b>123,00€</b> inkl. MwSt.</p><div class="buttons"><span class="btn details">DETAILS</span><span class="btn add">IN DEN WARENKORB</span></div></div>

<!-- footer -->
<div class="abs footer-band"></div>
<footer class="abs footer">
  <h4 style="left:239px"><span>WELLENBRETT</span> SITEMAP</h4>
  <ul class="flist" style="left:239px"><li>Home</li><li>Decks</li><li>Zubehör</li><li>Sale</li></ul>
  <ul class="flist" style="left:283px"><li>Team</li><li>Bilder</li><li>Kontakt</li><li>AGB</li></ul>
  <ul class="flist" style="left:326px"><li>Mein Konto</li><li>Datenschutz</li><li>Merkzettel</li><li>Impressum</li></ul>

  <h4 style="left:454px"><span>WELLENBRETT</span> KONTAKT</h4>
  <ul class="flist" style="left:454px"><li>Wellenbrett GmbH</li><li>Brettweg 1</li><li>54321 Rollhausen</li><li>Deutschland</li></ul>
  <ul class="flist" style="left:562px"><li>T: 04321 - 55 66 01 20 30</li><li>F: 04321 - 55 66 02 20 31</li><li>M: <a href="#">info@wellenbrett-shop.de</a></li><li>W: <a href="#">www.wellenbrett-shop.de</a></li></ul>

  <h4 style="left:749px"><span>WELLENBRETT</span> VERSANDINFOS</h4>
  <p class="ftext">Lorem Ipsum. Proin gravida nibh vel velit auctor aliquet. Aenean sollicitudin, lorem quis bibendum auctor, nisi elit consequat ipsum, nec sagittis sem nibh id elit. Duis sed odio sit amet nibh vulputate cursus a sit amet mauris.</p>
</footer>
<div class="abs copyright">Copyright © 2013 Wellenbrett &nbsp;|&nbsp; Alle Rechte vorbehalten.</div>

</body>
</html>
```